Stationary for a computer tech, hardware selling & website building & hosting for smb's
Pavillon Informatique
Professional
Mathieu Ostrowel
Directeur associé
4187 Boul. Lanvoisier Est
Montréal (Qc) H7T 8W2
514.555.0148 p.317
mathieu@pavillon-exemple.ca
www.pavillon-exemple.ca
Logo on white background
Logo on black background

```html
<!DOCTYPE html>
<html lang="fr">
<head>
<meta charset="utf-8">
<title>Pavillon Informatique – Cartes professionnelles</title>
<link rel="stylesheet" href="https://fonts.googleapis.com/css2?family=Titillium+Web:wght@400;600;700&display=swap">
<style>
  :root {
    --page-bg: #e6e6e6;
    --card-light: #ffffff;
    --card-dark: #0d0d0d;
    --ink-dark: #3a3a3a;
    --ink-light: #f2f2f2;
    --muted-dark: #555555;
    --muted-light: #bdbdbd;
    --accent: #8cc63f;
    --mark-grey: #4a4a4a;
    --rule-light: #cfcfcf;
    --rule-dark: #3a3a3a;
  }
  * { box-sizing: border-box; margin: 0; padding: 0; }
  html, body {
    width: 1200px; height: 1009px; overflow: hidden;
    background: var(--page-bg);
    font-family: "Titillium Web", sans-serif;
  }
  .stage { position: relative; width: 1200px; height: 1009px; }

  .card {
    position: absolute;
    width: 780px; height: 446px;
    border-radius: 22px;
    box-shadow: 0 6px 18px rgba(0,0,0,.18);
    padding: 64px 70px;
    display: flex; flex-direction: column;
  }
  .card--dark  { left: 360px; top: 40px;  background: var(--card-dark);  color: var(--ink-light); }
  .card--light { left: 60px;  top: 523px; background: var(--card-light); color: var(--ink-dark); }

  .brand {
    display: flex; align-items: center; gap: 22px;
    margin-left: 150px;
  }
  .brand__dot {
    width: 74px; height: 74px; border-radius: 50%;
    background: var(--accent);
    flex: none;
  }
  .brand__name {
    font-size: 46px; font-weight: 600; letter-spacing: -0.5px; line-height: 1;
  }
  .card--light .brand__name { color: var(--ink-dark); }
  .card--dark  .brand__name { color: var(--ink-light); }

  .details {
    margin-top: auto;
    display: flex; align-items: stretch;
  }
  .person {
    width: 290px; text-align: right; padding-right: 30px;
    font-size: 19px; line-height: 1.35;
  }
  .person__name { font-weight: 700; font-size: 22px; }
  .person__role { color: var(--accent); font-weight: 600; margin-bottom: 8px; }
  .card--light .person__address { color: var(--muted-dark); }
  .card--dark  .person__address { color: var(--muted-light); }

  .divider { width: 1px; }
  .card--light .divider { background: var(--rule-light); }
  .card--dark  .divider { background: var(--rule-dark); }

  .contact {
    list-style: none; padding-left: 30px;
    font-size: 19px; line-height: 1.55;
  }
  .contact li { display: flex; align-items: center; gap: 12px; }
  .card--light .contact { color: var(--muted-dark); }
  .card--dark  .contact { color: var(--muted-light); }
  .icon { width: 16px; height: 16px; flex: none; fill: var(--accent); }
</style>
</head>
<body>
<main class="stage">

  <section class="card card--dark" aria-label="Carte, verso noir">
    <div class="brand">
      <span class="brand__dot"></span>
      <span class="brand__name">Pavillon Informatique</span>
    </div>
    <div class="details">
      <div class="person">
        <p class="person__name">Mathieu Ostrowel</p>
        <p class="person__role">Directeur associé</p>
        <p class="person__address">4187 Boul. Lanvoisier Est<br>Montréal (QC) H7T 8W2</p>
      </div>
      <span class="divider"></span>
      <ul class="contact">
        <li><svg class="icon" viewBox="0 0 16 16"><path d="M3 1l3 3-2 2c1 2 3 4 5 5l2-2 3 3-2 3C7 15 1 9 1 3z"/></svg>514.555.0148 p.317</li>
        <li><svg class="icon" viewBox="0 0 16 16"><rect x="4" y="0" width="8" height="16" rx="1.5"/></svg>514.555.0193</li>
        <li><svg class="icon" viewBox="0 0 16 16"><rect x="4" y="1" width="8" height="5"/><rect x="1" y="6" width="14" height="7" rx="1"/></svg>514.555.0127</li>
        <li><svg class="icon" viewBox="0 0 16 16"><path d="M0 3h16v10H0zM1 4l7 5 7-5" stroke="#0d0d0d" stroke-width="1"/></svg>mathieu@pavillon-exemple.ca</li>
        <li><svg class="icon" viewBox="0 0 16 16"><circle cx="8" cy="8" r="8"/></svg>www.pavillon-exemple.ca</li>
      </ul>
    </div>
  </section>

  <section class="card card--light" aria-label="Carte, recto blanc">
    <div class="brand">
      <span class="brand__dot"></span>
      <span class="brand__name">Pavillon Informatique</span>
    </div>
    <div class="details">
      <div class="person">
        <p class="person__name">Mathieu Ostrowel</p>
        <p class="person__role">Directeur associé</p>
        <p class="person__address">4187 Boul. Lanvoisier Est<br>Montréal (QC) H7T 8W2</p>
      </div>
      <span class="divider"></span>
      <ul class="contact">
        <li><svg class="icon" viewBox="0 0 16 16"><path d="M3 1l3 3-2 2c1 2 3 4 5 5l2-2 3 3-2 3C7 15 1 9 1 3z"/></svg>514.555.0148 p.317</li>
        <li><svg class="icon" viewBox="0 0 16 16"><rect x="4" y="0" width="8" height="16" rx="1.5"/></svg>514.555.0193</li>
        <li><svg class="icon" viewBox="0 0 16 16"><rect x="4" y="1" width="8" height="5"/><rect x="1" y="6" width="14" height="7" rx="1"/></svg>514.555.0127</li>
        <li><svg class="icon" viewBox="0 0 16 16"><path d="M0 3h16v10H0zM1 4l7 5 7-5" stroke="#ffffff" stroke-width="1"/></svg>mathieu@pavillon-exemple.ca</li>
        <li><svg class="icon" viewBox="0 0 16 16"><circle cx="8" cy="8" r="8"/></svg>www.pavillon-exemple.ca</li>
      </ul>
    </div>
  </section>

</main>
</body>
</html>
```